Quillbrook Builders Business Cards

I want to use the logo and make an unique business card that shows the textured Logo with brick and builings. I want to be able to stand out when I pass out business cards.

```html
<!DOCTYPE html>
<html lang="en">
<head>
<meta charset="utf-8">
<title>Quillbrook Builders Business Cards</title>
<link href="https://fonts.googleapis.com/css2?family=Oswald:wght@500;700&family=Lato:wght@400;700&display=swap" rel="stylesheet">
<style>
  :root {
    --page: #2b2b2b;
    --concrete-light: #d9dad4;
    --concrete-mid: #c3c4bd;
    --concrete-dark: #9a9b94;
    --brick: #c8452b;
    --ink: #16161a;
    --navy: #1c2540;
    --text: #2c2c2c;
    --rule: #6f706b;
  }
  * { margin: 0; padding: 0; box-sizing: border-box; }
  html, body { width: 1200px; height: 875px; overflow: hidden; }
  body {
    background: var(--page);
    display: flex;
    flex-direction: column;
    align-items: center;
    justify-content: center;
    gap: 36px;
    font-family: "Lato", sans-serif;
  }
  .card {
    width: 660px;
    height: 377px;
    border-radius: 22px;
    position: relative;
    overflow: hidden;
    box-shadow: 0 14px 30px rgba(0,0,0,.45);
  }
  .card-texture {
    position: absolute; inset: 0;
    background:
      radial-gradient(ellipse at 65% 25%, var(--concrete-light) 0%, var(--concrete-mid) 55%, var(--concrete-dark) 100%);
  }
  .logo-block {
    position: absolute;
    display: flex;
    flex-direction: column;
    align-items: center;
  }
  .logo-mark {
    display: flex; align-items: center; gap: 12px;
  }
  .logo-square { width: 30px; height: 30px; background: var(--brick); }
  .logo-name {
    font-family: "Oswald", sans-serif;
    font-weight: 700;
    color: var(--brick);
    text-transform: uppercase;
    line-height: 1;
  }
  .tagline {
    font-family: "Oswald", sans-serif;
    font-weight: 500;
    color: var(--navy);
    margin-top: 18px;
  }
  /* front */
  .card-front .logo-block { left: 0; right: 0; top: 118px; }
  .card-front .logo-name { font-size: 46px; }
  .card-front .tagline { font-size: 17px; }
  /* back */
  .card-back .logo-block { left: 28px; width: 330px; top: 140px; }
  .card-back .logo-name { font-size: 34px; }
  .card-back .logo-square { width: 24px; height: 24px; }
  .card-back .tagline { font-size: 14px; }
  .divider {
    position: absolute; left: 372px; top: 92px; width: 1px; height: 210px;
    background: var(--rule);
  }
  .contact {
    position: absolute; left: 392px; top: 80px; right: 20px;
    color: var(--text);
  }
  .person-name {
    font-family: "Oswald", sans-serif; font-weight: 700;
    font-size: 32px; color: var(--ink); letter-spacing: 1px; line-height: 1.1;
  }
  .person-role { color: var(--brick); font-size: 15px; margin-bottom: 12px; }
  .contact-list { list-style: none; font-size: 14px; line-height: 1.45; }
  .contact-list li { display: flex; align-items: flex-start; gap: 10px; }
  .contact-list svg { width: 12px; height: 12px; flex: none; margin-top: 4px; fill: var(--brick); }
  .contact-list .address { margin-bottom: 6px; }
</style>
</head>
<body>

<section class="card card-front">
  <div class="card-texture" role="img" aria-label="Grey cracked concrete texture"></div>
  <div class="logo-block">
    <div class="logo-mark">
      <span class="logo-square"></span>
      <span class="logo-name">Quillbrook Builders</span>
    </div>
    <p class="tagline">Patios - Sidewalks - Retaining Walls - Foundations</p>
  </div>
</section>

<section class="card card-back">
  <div class="card-texture" role="img" aria-label="Grey cracked concrete texture"></div>
  <div class="logo-block">
    <div class="logo-mark">
      <span class="logo-square"></span>
      <span class="logo-name">Quillbrook Builders</span>
    </div>
    <p class="tagline">Patios - Sidewalks - Retaining Walls - Foundations</p>
  </div>
  <div class="divider"></div>
  <div class="contact">
    <h1 class="person-name">OWEN HARTLEY</h1>
    <p class="person-role">Founder &amp; CEO</p>
    <ul class="contact-list">
      <li class="address">
        <svg viewBox="0 0 12 12"><path d="M6 0a4 4 0 0 0-4 4c0 3 4 8 4 8s4-5 4-8a4 4 0 0 0-4-4zm0 5.5A1.5 1.5 0 1 1 6 2.5a1.5 1.5 0 0 1 0 3z"/></svg>
        <span>Street Address Here, City<br>State, Country, ZIP 123</span>
      </li>
      <li>
        <svg viewBox="0 0 12 12"><path d="M2.5 0.5l2 2.5-1.2 1.3a7 7 0 0 0 4.4 4.4L9 7.5l2.5 2-1.5 2C5 11.5 0.5 7 0.5 2z"/></svg>
        <span>(555) 014-2290</span>
      </li>
      <li>
        <svg viewBox="0 0 12 12"><path d="M3 0h6a1 1 0 0 1 1 1v10a1 1 0 0 1-1 1H3a1 1 0 0 1-1-1V1a1 1 0 0 1 1-1zm0 1.5v8h6v-8z"/></svg>
        <span>(555) 014-2291</span>
      </li>
      <li>
        <svg viewBox="0 0 12 12"><path d="M3 0h6v3H3zM1 4h10v5H9v3H3V9H1zm3 5v2h4V9z"/></svg>
        <span>(555) 014-2292</span>
      </li>
      <li>
        <svg viewBox="0 0 12 12"><path d="M0 2h12v1L6 7 0 3zm0 2.5l6 4 6-4V10H0z"/></svg>
        <span>info@quillbrookbuilders.com</span>
      </li>
      <li>
        <svg viewBox="0 0 12 12"><circle cx="6" cy="6" r="6"/></svg>
        <span>quillbrookbuilders.com</span>
      </li>
    </ul>
  </div>
</section>

</body>
</html>
```